OLU58 biz card & Stationery

LU58 is a personalized shopping experience brought to you, that lets you find and discover fashion goods through a collection of boutiques curated by taste-makers - celebrities, stylists, designers, and fashion bloggers. Boutiques uses visual technology to help fashionistas discover and shop their look and creates the opportunity for designers to showcase their collections and latest inspirations online.

OLU58 is built on technology developed by our team of fashion experts who work with engineers to “teach” our computer systems to understand various patterns, pairings, and genre definitions. When signed into your account, OLU58 learns about your style and preferences and in turn, provides you better results and recommendations over time. Ultimately, OLU58 will provide shoppers with a much richer and interactive shopping experience and help drive traffic to retailers' websites.

We need a definitely cool business card. The card must be black! And must use our official logo which can be download from OLU58.com

The address for Letter head and evenlop, please use 4872 Crestwick Parkway, Sutie 510 Los Angeles CA90412, email will be anyone@OLU58.com, website is www.OLU58.com

thanks

We received some of the design, thanks. But most of the design are not what we want. We need a very clean version with black ground, you may also use some dark gray to add the element. please take a look at http://morvalstudio.no/work/#pelter__ostrama/, we do like this kind of design very much. hope it help.

```html
<!DOCTYPE html>
<html lang="en">
<head>
<meta charset="utf-8">
<title>OLU58 Letterhead</title>
<link rel="stylesheet" href="https://fonts.googleapis.com/css2?family=Jost:wght@400;600&display=swap">
<style>
  :root {
    --page-bg: #ffffff;
    --sheet-bg: #ffffff;
    --sheet-edge: #1a1a1a;
    --band: #000000;
    --accent-gray: #4a4a4a;
    --ink-light: #ffffff;
    --ink-dark: #111111;
  }
  * { margin: 0; padding: 0; box-sizing: border-box; }
  html, body {
    width: 1200px;
    height: 900px;
    overflow: hidden;
    background: var(--page-bg);
    font-family: "Jost", sans-serif;
  }
  .canvas {
    position: relative;
    width: 1200px;
    height: 900px;
  }
  .letterhead {
    position: absolute;
    left: 322px;
    top: 32px;
    width: 560px;
    height: 774px;
    background: var(--sheet-bg);
    border: 2px solid var(--sheet-edge);
  }
  .letterhead__band {
    position: absolute;
    left: 0;
    top: 0;
    width: 100%;
    height: 110px;
    background: var(--band);
  }
  .brand-name {
    position: absolute;
    left: 12px;
    top: 10px;
    font-size: 26px;
    font-weight: 600;
    line-height: 1;
    color: var(--ink-light);
  }
  .accent-bar {
    position: absolute;
    left: 368px;
    top: 0;
    width: 16px;
    height: 52px;
    background: var(--accent-gray);
  }
  .address {
    position: absolute;
    left: 390px;
    top: 56px;
    font-style: normal;
    font-size: 8.5px;
    font-weight: 600;
    line-height: 13px;
    color: var(--ink-light);
  }
  .caption {
    position: absolute;
    left: 0;
    width: 1200px;
    top: 830px;
    text-align: center;
    font-size: 30px;
    font-weight: 400;
    color: var(--ink-dark);
  }
</style>
</head>
<body>
  <main class="canvas">
    <section class="letterhead">
      <header class="letterhead__band">
        <div class="brand-name">OLU58</div>
        <div class="accent-bar"></div>
        <address class="address">
          4872 Crestwick Parkway,<br>
          Sutie 510 Los Angeles CA90412<br>
          www.OLU58.com
        </address>
      </header>
    </section>
    <p class="caption">letterhead</p>
  </main>
</body>
</html>
```